Business Cards

We were billed for this because the project timed out. Please give me another designed to open this back up. I was not happy with the last designs (that I was charged for).
we are also using the logo with Revitalizing Pools One Drop at a Time
Also want to utilize Where Healthy Water is our Commitment.

Contact Information for Business Card

Marlowe Stone Group Inc

```html
<!DOCTYPE html>
<html lang="en">
<head>
<meta charset="utf-8">
<title>Marlowe Stone Group – Business Cards</title>
<link href="https://fonts.googleapis.com/css2?family=Barlow:wght@400;500;700&display=swap" rel="stylesheet">
<style>
  :root{
    --bg-blue:#0f6db3;
    --brand-blue:#1269b0;
    --card:#ffffff;
    --ink:#414244;
  }
  *{margin:0;padding:0;box-sizing:border-box}
  html,body{width:1200px;height:1096px;overflow:hidden}
  body{background:var(--bg-blue);position:relative;font-family:"Barlow",Arial,sans-serif;color:var(--ink)}
  .card{position:absolute;left:217px;width:765px;height:428px;background:var(--card);border-radius:27px}
  .card--front{top:112px}
  .card--back{top:603px}

  .brand{position:absolute;text-align:center;white-space:nowrap;width:315px}
  .brand__name{font-weight:700;font-size:25px;letter-spacing:1.5px;text-transform:uppercase;line-height:1}
  .card--front .brand{left:72px;top:154px}
  .card--back .brand{left:225px;top:192px}

  .person{position:absolute;left:443px;top:71px;width:32px;height:41px}
  .contact-name{position:absolute;left:495px;top:82px;font-size:20px;font-weight:500;letter-spacing:.4px}

  .icon-rail{position:absolute;left:451px;top:182px;width:30px;height:113px;background:var(--brand-blue);border-radius:6px}
  .icon-rail svg{position:absolute;left:7px;width:16px;height:16px}
  .contact-line{position:absolute;left:502px;font-size:18.5px;font-weight:500;letter-spacing:.4px;line-height:1}
  .contact-line--phone{top:194px}
  .contact-line--mail{top:229px}
  .contact-line--web{top:265px}
  .address{position:absolute;left:451px;top:316px;font-size:17px;font-weight:500;line-height:23px;letter-spacing:.3px;font-style:normal}

  .web-spaced{position:absolute;left:0;width:765px;top:356px;text-align:center;font-size:14px;font-weight:500;letter-spacing:10px;padding-left:10px}
</style>
</head>
<body>
  <section class="card card--front">
    <div class="brand">
      <div class="brand__name">Marlowe Stone Group</div>
    </div>

    <svg class="person" viewBox="0 0 32 41" aria-hidden="true">
      <rect x="8" y="0" width="16" height="20" rx="8" fill="var(--brand-blue)"/>
      <path d="M0 41 V31 Q0 22 9 21 Q16 27 23 21 Q32 22 32 31 V41 Q16 43 0 41Z" fill="var(--brand-blue)"/>
    </svg>
    <div class="contact-name">your name</div>

    <div class="icon-rail">
      <svg viewBox="0 0 16 16" style="top:14px" aria-hidden="true">
        <path d="M3 1.5 L5.5 1 L7 4.5 L5.3 6 Q6.5 9 10 10.7 L11.5 9 L15 10.5 L14.5 13 Q13 15 10 14 Q3 11 2 5 Q1.8 2.5 3 1.5Z" fill="#fff"/>
      </svg>
      <svg viewBox="0 0 16 16" style="top:49px" aria-hidden="true">
        <rect x="1" y="3.5" width="14" height="9.5" fill="#fff"/>
        <path d="M1.5 4 L8 9 L14.5 4 M1.5 12.5 L6 8 M14.5 12.5 L10 8" stroke="var(--brand-blue)" stroke-width="1" fill="none"/>
      </svg>
      <svg viewBox="0 0 16 16" style="top:85px" aria-hidden="true">
        <g fill="none" stroke="#fff" stroke-width="1.2">
          <circle cx="8" cy="8" r="6.5"/>
          <ellipse cx="8" cy="8" rx="3" ry="6.5"/>
          <path d="M1.5 8 H14.5 M8 1.5 V14.5 M2.6 4.8 H13.4 M2.6 11.2 H13.4"/>
        </g>
      </svg>
    </div>
    <div class="contact-line contact-line--phone">+000 123 456 7890</div>
    <div class="contact-line contact-line--mail">yourgmail@name.com</div>
    <div class="contact-line contact-line--web">www.websitename.com</div>

    <address class="address">your street address place here<br>new yerk city, zip code - 000</address>
  </section>

  <section class="card card--back">
    <div class="brand">
      <div class="brand__name">Marlowe Stone Group</div>
    </div>
    <div class="web-spaced">www.websitename.com</div>
  </section>
</body>
</html>
```